Poster Needed for Church Conference

I need a poster for a weekend conference at my church. Looking to attract as many people as possible. We are a church in the suburbs of Houston. This is mainly for our own church members but we are opening it up to outside church members.

Please see previous design from last conference and all other graphic work that can (doesn't need to be) included.

Target Market(s)

It's targeted for all people. But our main audience is families. around the age of 30 should be main target.

Industry/Entity Type

Non-Profit

Font styles to use
Serif
Sans Serif

Colors

Designer to choose colors to be used in the design.

Requirements
Must have
• 11x17 design with ability to shrink and blow up. but ideally for 11x17
• Content and wording:
• "Rooted Lantern Conference: Bridging the gap between generations and passing on our deepest beliefs and values."
• Featuring Dr. Glen Marlowe. Author of "The Map of Q9"
• Aug 25-26: Friday 8-10 pm, Saturday 4-8 pm
• Cost Adults $15/Children $5: Covers admission to all sessions and workshops, refreshments and Saturday dinner. *kids 5 and under free
• Childcare provided for all sessions. "
• Please use church logo and address on flyer: 4312 Orchard Bend, Missouri City, TX 77512
Nice to have
• Ideally it will be designed so that we can crop a 16:9 pp announcement slide and header for our website.
Should not have
• anything offensive

```html
<!DOCTYPE html>
<html lang="en">
<head>
<meta charset="utf-8">
<title>Rooted Lantern Conference Poster</title>
<link href="https://fonts.googleapis.com/css2?family=Bebas+Neue&family=Montserrat:wght@500;600;700;800&display=swap" rel="stylesheet">
<style>
:root{
  --navy:#1b2e4b;
  --teal:#2fb6cf;
  --sky:#3cb4e6;
  --green:#3aaa48;
  --lime:#b7d63a;
  --blue:#1f6fb8;
  --paper:#ffffff;
  --backdrop:#e9ecef;
}
*{margin:0;padding:0;box-sizing:border-box}
html,body{width:1200px;height:1200px;overflow:hidden;background:var(--backdrop)}
.poster{position:absolute;left:30px;top:220px;width:1140px;height:760px;background:var(--paper);overflow:hidden;font-family:'Montserrat',sans-serif;color:var(--navy)}
.art{position:absolute;left:0;top:0}
.crystals-top{left:0;top:0;width:440px;height:360px}
.crystals-corner{left:auto;right:0;top:auto;bottom:0;width:260px;height:220px}
.speaker-photo{left:204px;top:244px;width:226px;height:220px}
.book-cover{left:822px;top:200px;width:140px;height:210px;background:linear-gradient(160deg,#f4f5f6,#d9dcdf);box-shadow:4px 6px 12px rgba(0,0,0,.2)}
.title{position:absolute;left:422px;top:52px;font-size:45px;font-weight:800;letter-spacing:-1px;white-space:nowrap}
.subtitle{position:absolute;left:424px;top:112px;font-size:27px;font-weight:500;color:var(--teal);line-height:1.4;letter-spacing:-.5px;white-space:nowrap}
.feature{position:absolute;left:440px;top:318px;white-space:nowrap}
.feature h2{font-size:26px;font-weight:800;color:var(--green);letter-spacing:-.6px}
.feature p{font-size:14.5px;font-weight:500;color:var(--green);line-height:1.35;margin-top:4px}
.cost{position:absolute;left:442px;top:436px;width:580px}
.cost h3{font-size:26px;font-weight:800;letter-spacing:-.6px}
.cost .price{font-family:'Bebas Neue',sans-serif;font-weight:400;color:var(--sky);font-size:44px;letter-spacing:0}
.cost p{font-size:16px;font-weight:600;line-height:1.4;letter-spacing:-.3px}
.cost .free{color:var(--sky);font-weight:500}
.cost .free b{font-weight:800}
.cost .childcare{margin-top:22px}
.dates{position:absolute;left:60px;top:466px;width:260px;text-align:center;font-family:'Bebas Neue',sans-serif;white-space:nowrap}
.dates .month{font-size:64px;line-height:.95}
.dates .days{font-size:112px;line-height:.9;color:var(--sky)}
.dates .times{font-size:26px;line-height:1.15;margin-top:4px}
.church{position:absolute;left:650px;top:604px;white-space:nowrap}
.church .name{display:flex;align-items:center;gap:10px;font-size:23px;font-weight:600;color:var(--green);line-height:1.1}
.church .mark{width:32px;height:32px;background:var(--green);flex:none}
.church .address{font-size:13px;font-weight:700;color:var(--blue);margin-top:8px}
</style>
</head>
<body>
<main class="poster">
  <svg class="art crystals-top" viewBox="0 0 440 360" role="img" aria-label="Cluster of faceted blue and green crystal shapes">
    <defs>
      <linearGradient id="crystalGrad" x1="0" y1="0" x2="1" y2="1">
        <stop offset="0" stop-color="#2f8fd8"/>
        <stop offset=".55" stop-color="#3cc0c8"/>
        <stop offset="1" stop-color="#b7d63a"/>
      </linearGradient>
    </defs>
    <polygon points="0,0 420,0 360,110 300,200 250,300 200,250 60,330 0,280" fill="url(#crystalGrad)"/>
  </svg>
  <svg class="art speaker-photo" viewBox="0 0 226 220" role="img" aria-label="Portrait photo of speaker Dr. Glen Marlowe in a triangle frame">
    <defs>
      <linearGradient id="photoGrad" x1="0" y1="0" x2="1" y2="0">
        <stop offset="0" stop-color="#2a2a2a"/>
        <stop offset="1" stop-color="#c99a80"/>
      </linearGradient>
    </defs>
    <polygon points="0,115 180,0 200,220" fill="url(#photoGrad)"/>
    <polygon points="180,0 226,120 200,220" fill="#3ab0c9"/>
  </svg>
  <div class="art book-cover" role="img" aria-label="Book cover of The Map of Q9 by Dr. Glen Marlowe"></div>

  <h1 class="title">Rooted Lantern Conference:</h1>
  <p class="subtitle">Bridging the gap between generations and<br>passing on our deepest beliefs and values.</p>

  <section class="feature">
    <h2>Featuring Dr. Glen Marlowe.</h2>
    <p>Author of Map of Q9, Founder of Q9 Ministries<br>and Expert in Parent/Children relationships.</p>
  </section>

  <section class="cost">
    <h3>Cost : Adults <span class="price">$15,</span> Children <span class="price">$5:</span></h3>
    <p>Covers admission to all sessions and workshops, refreshments and Saturday dinner. <span class="free">*kids 5 and under <b>FREE</b></span></p>
    <p class="childcare">Childcare provided for all sessions.</p>
  </section>

  <section class="dates">
    <div class="month">August</div>
    <div class="days">25-26</div>
    <div class="times">Friday 8-10 PM<br>Saturday 4-8 PM</div>
  </section>

  <section class="church">
    <div class="name"><span class="mark"></span><span>cedar hollow<br>community church</span></div>
    <div class="address">#4312 Orchard Bend, Missouri City, TX 77512</div>
  </section>

  <svg class="art crystals-corner" viewBox="0 0 260 220" role="img" aria-label="Faceted blue and green crystal shapes in the corner">
    <defs>
      <linearGradient id="cornerGrad" x1="0" y1="1" x2="1" y2="0">
        <stop offset="0" stop-color="#b7d63a"/>
        <stop offset=".5" stop-color="#3cc0c8"/>
        <stop offset="1" stop-color="#2f8fd8"/>
      </linearGradient>
    </defs>
    <polygon points="260,0 260,220 40,220 80,190 150,150 180,80 230,40" fill="url(#cornerGrad)"/>
  </svg>
</main>
</body>
</html>
```